TriFold Brochure

I would like to have my brochure redesigned so that it has the same look and feel as our website, at www.glintridgeautospa.com. I would like to keep it as a tri-fold, color brochure.

• similar look and feel as website design. www.glintridgeautospa.com

should include and play up the eco-friendly experience since we are fully eco-friendly from the ground up.

```html
<!DOCTYPE html>
<html lang="en">
<head>
<meta charset="utf-8">
<title>Glintridge Auto Spa – Tri-Fold Brochure</title>
<link rel="stylesheet" href="https://fonts.googleapis.com/css2?family=Titan+One&family=PT+Serif:wght@400;700&display=swap">
<style>
  :root {
    --blue-deep: #1f4fc4;
    --blue-light: #4d86ea;
    --green-deep: #2fbf2a;
    --green-light: #6be85e;
    --paper: #ffffff;
    --ink: #111111;
    --head-green: #3fe334;
    --head-blue: #1d56e0;
    --head-stroke: #0c220c;
    --rule: #111111;
  }
  * { margin: 0; padding: 0; box-sizing: border-box; }
  html, body { width: 1200px; height: 849px; overflow: hidden; background: var(--paper); }
  .brochure {
    position: relative; width: 1200px; height: 849px; overflow: hidden;
    font-family: "PT Serif", Georgia, serif; font-size: 15.6px; line-height: 20.5px; color: var(--ink);
    hyphens: auto; -webkit-hyphens: auto;
  }
  .backdrop { position: absolute; inset: 0; }
  .fold-rule { position: absolute; top: 0; width: 2px; height: 849px; background: var(--rule); }
  .fold-rule.first { left: 403px; }
  .fold-rule.second { left: 804px; }
  .block { position: absolute; }
  .heading {
    font-family: "Titan One", "Arial Black", sans-serif; font-weight: 400;
    color: var(--head-green); -webkit-text-stroke: 1px var(--head-stroke);
    text-shadow: 2px 2px 2px rgba(0,0,0,.55); text-transform: uppercase;
    font-size: 17px; line-height: 20px; letter-spacing: .3px; text-align: center;
    hyphens: none; -webkit-hyphens: none; white-space: nowrap;
  }
  .heading.title-case { text-transform: none; }
  .heading.blue { color: var(--head-blue); }
  .tagline {
    position: absolute; left: 28px; top: 36px; width: 330px;
    font-size: 26px; line-height: 32px; text-align: center;
    transform: rotate(-8.5deg); transform-origin: center center;
  }
  .indent p { text-indent: 50px; }
  .indent p + p { margin-top: 20px; }
  .right { text-align: right; }
  .service-name { font-weight: 700; }
  .price-list { width: 348px; hyphens: none; -webkit-hyphens: none; }
  .price-row { display: flex; justify-content: space-between; }
  .car-art { position: absolute; left: 700px; top: 400px; width: 440px; height: 245px; }
</style>
</head>
<body>
<main class="brochure">
  <svg class="backdrop" width="1200" height="849" viewBox="0 0 1200 849" aria-hidden="true">
    <defs>
      <linearGradient id="blueBand" x1="0" y1="0" x2="0" y2="1">
        <stop offset="0" stop-color="#4d86ea"/>
        <stop offset="1" stop-color="#1f4fc4"/>
      </linearGradient>
      <linearGradient id="greenBand" x1="0" y1="0" x2="0" y2="1">
        <stop offset="0" stop-color="#6be85e"/>
        <stop offset="1" stop-color="#2fbf2a"/>
      </linearGradient>
    </defs>
    <polygon points="0,0 1200,0 1200,110 0,345" fill="url(#blueBand)"/>
    <polygon points="0,455 1200,780 1200,849 0,849" fill="url(#greenBand)"/>
  </svg>

  <div class="fold-rule first"></div>
  <div class="fold-rule second"></div>

  <h1 class="heading title-case tagline">Go Green. Get Clean.<br>The Smart Way.</h1>
  <section class="block indent" style="left:10px; top:112px; width:372px;">
    <p>The Glintridge Auto Spa lives up to its name by caring for the environment in every part of our business. We strive to be the world’s most eco-friendly car wash and detail service.</p>
    <p>By washing your car at Glintridge Auto Spa, not only are you getting a clean and shiny vehicle, but together we can make a difference in protecting the environment.</p>
  </section>

  <h2 class="block heading title-case" style="left:185px; top:314px; font-size:24px; line-height:28px;">Fundraisers</h2>
  <section class="block right" style="left:52px; top:348px; width:333px;">
    <p>Our community is important to us and we take pride in working with our community to fundraise for a good cause. We make fundraising fun for youth groups, teams, scouts, and clubs. Contact us today to learn how to team up with us and raise money for your organization.</p>
  </section>

  <h2 class="block heading title-case blue" style="left:38px; top:557px; font-size:24px; line-height:28px;">School Trips</h2>
  <section class="block" style="left:24px; top:626px; width:328px;">
    <p>Make learning about environmental responsibility fun with a field trip. We explain the power of efficient energy use, water recycling, and safe chemicals. We host class sizes up to 30 and every student, teacher, and bus driver will take home a real life lesson and a free car wash coupon.</p>
  </section>

  <h2 class="block heading" style="left:404px; top:34px; width:400px;">Gift Cards</h2>
  <p class="block" style="left:410px; top:54px; width:372px;">The perfect gift for anyone! Gift cards can be used for both wash and detailing services!</p>
  <h2 class="block heading" style="left:404px; top:116px; width:400px;">Military Support</h2>
  <p class="block" style="left:410px; top:138px; width:372px;">We support military &amp; active veterans by offering special discounts.</p>

  <h2 class="block heading" style="left:404px; top:260px; width:400px;">VIP Club</h2>
  <p class="block" style="left:410px; top:302px; width:368px;">The Green &amp; Good Value club provides you with great benefits including special offers, exclusive deals and free car washes. It’s free and easy to enroll. Join our FREE membership club to receive fantastic benefits including free wash during your birthday week, 10% off detail services and your 10th wash free.</p>

  <div class="car-art" role="img" aria-label="Illustration of a red sports car">
    <svg width="440" height="245" viewBox="0 0 440 245" aria-hidden="true">
      <defs>
        <radialGradient id="carTone" cx=".55" cy=".5" r=".6">
          <stop offset="0" stop-color="#f08a8a" stop-opacity=".85"/>
          <stop offset=".7" stop-color="#f3a9a9" stop-opacity=".55"/>
          <stop offset="1" stop-color="#ffffff" stop-opacity="0"/>
        </radialGradient>
      </defs>
      <ellipse cx="230" cy="130" rx="220" ry="115" fill="url(#carTone)"/>
    </svg>
  </div>

  <h2 class="block heading" style="left:404px; top:466px; width:400px;">Wash Services</h2>
  <section class="block" style="left:410px; top:507px; width:378px;">
    <p class="service-name">Platinum Ultimate $36.99</p>
    <p>Platinum Service PLUS HOT WAX</p>
    <p class="service-name">Platinum Full Service $24.99</p>
    <p>Gold Service PLUS • Tire Shine • Wheels/Rims • Lemon • Glo Wax • Cherry Burst Sealant • Fragrance</p>
    <p class="service-name">Gold Full Service $19.99</p>
    <p>Exterior Wash • Triple Foam • Vacuum Interior • Dash • Windows • Underbody • Clear Coat Sealant</p>
    <p class="service-name">Exterior Ultimate $24.99</p>
    <p>Exterior Xpress PLUS • Hot Wax</p>
    <p class="service-name">Exterior Xpress Plus $12.99</p>
    <p>Exterior Wash • Triple Foam • Underbody • Clear Coat Sealant • Wash and Dry</p>
    <p class="service-name">Exterior Xpress $9.99</p>
    <p>Exterior Wash • Cloth Wash • Turbo Air Dry</p>
  </section>

  <h2 class="block heading" style="left:820px; top:34px;">Unlimited Wash Packages</h2>
  <p class="block" style="left:820px; top:55px; width:275px;">Wash as often as you’d like for one low monthly fee. No waiting in lines. Make it shine all the time.</p>
  <section class="block right service-name" style="left:870px; top:138px; width:298px;">
    <p>Exterior Only $24.99/mth</p>
    <p>Full Service $34.99/mth</p>
    <p>Car Freak Service $59.99/mth</p>
  </section>

  <h2 class="block heading title-case" style="left:805px; top:228px; width:395px; font-size:25px; line-height:30px;">Detail Services</h2>
  <h3 class="block heading" style="left:805px; top:280px; width:395px;">Interior Detail Services</h3>
  <section class="block price-list" style="left:820px; top:321px;">
    <div class="price-row"><span>Interior Super Clean</span><span>$34.99</span></div>
    <div class="price-row"><span>Express Upholstery/Leather Cleaning</span><span>$39.99</span></div>
    <div class="price-row"><span>Express Carpet Cleaning</span><span>$49.99</span></div>
    <div class="price-row"><span>Rid Odor Treatment</span><span>$49.99</span></div>
  </section>

  <h3 class="block heading" style="left:805px; top:424px; width:395px;">Exterior Detail Services</h3>
  <section class="block price-list" style="left:820px; top:465px;">
    <div class="price-row"><span>Lustrel Body Gloss</span><span>$9.99</span></div>
    <div class="price-row"><span>Lustrel Express Wash</span><span>$39.99</span></div>
    <div class="price-row"><span>Lustrel Super Wax</span><span>$49.99</span></div>
    <div class="price-row"><span>Paint Sealant</span><span>$99.99</span></div>
    <div class="price-row"><span>2 Step Cleaning</span><span>$69.99</span></div>
    <div class="price-row"><span>Express Clay Service</span><span>$39.99</span></div>
    <div class="price-row"><span>Clearvue Glass Treatment</span><span>$9.99</span></div>
    <div class="price-row"><span>Headlight Restoration</span><span>$39.99</span></div>
    <div class="price-row"><span>Bumper to Bumper Detail starting at</span><span>$180</span></div>
  </section>

  <h3 class="block heading" style="left:805px; top:670px; width:395px;">A La Carte Services</h3>
  <section class="block price-list" style="left:820px; top:711px;">
    <div class="price-row"><span>Rims</span><span>$4.99</span></div>
    <div class="price-row"><span>Body Gloss</span><span>$9.99</span></div>
    <div class="price-row"><span>Tire Shine</span><span>$3.99</span></div>
    <div class="price-row"><span>Hot Wax</span><span>$13.99</span></div>
    <div class="price-row"><span>Vacuum</span><span>$4.99</span></div>
  </section>
</main>
</body>
</html>
```